Keystone Vault Depot Services Needs A Website

We are looking for a website for a new company. 4 Pages

Needs to be responsive and mobile friendly for all browsers and coded for both Android & IOS. SEO is also important.

Website Brief – Keystone Vault Depot Services
Domain: www.keystonevaultdepot.com
Email: info@keystonevaultdepot.com
Phone: to be inserted later
Address: 10458 82 Ave, Edmonton, AB T6E 2K9
Platform: WordPress (recommended for flexibility, SEO tools, and ease of editing)
Requirements:
• Responsive & mobile-friendly (Android & iOS)
• Cross-browser compatibility
• Fast page load speed
• SEO optimized for storage development, management, and investment keywords
• Easy in-house editing after launch
• Professional, modern, trust-driven design reflecting expertise, reliability, and innovation
________________________________________
Pages
1. HOME
Purpose: Quickly communicate who Keystone Vault Depot Services is and why they’re the best choice for designing, building, leasing, and managing self storage facilities.
Content Highlights:
• Hero Section: Large, bold image of a modern self storage facility with headline:
"From Concept to Capacity – Your Self Storage Experts"
• Subheadline: “Keystone Vault Depot Services delivers turnkey design, construction, leasing, and management services for profitable self storage operations.”
• Quick Service Icons:
o Facility Design & Development
o Construction & Build Management
o Lease-Up & Marketing
o Ongoing Facility Management
• Call to Action Button: “LEARN MORE” → links to ABOUT US page.
• Featured Project Highlights: Showcase a few completed or current projects with photos and stats.
• Contact Banner: “Ready to build your next self storage project? Let’s talk.” → CONTACT page.
2. ABOUT US
Purpose: Build credibility, showcase experience, and explain the value proposition.
Content Highlights:
• Who We Are: Overview of Keystone Vault Depot Services’ history, mission, and team expertise.
• Our Approach: End-to-end process from site selection to occupancy.
• Why Choose Us:
o Industry expertise in self storage
o Proven track record in lease-up success
o Strong vendor and contractor network
3. SERVICES
Purpose: Detail all service offerings with clarity and authority.
Sections:
• Design & Development: Market analysis, site planning, and architectural design.
• Construction Management: Overseeing timelines, budgets, and quality control.
• Lease-Up Strategy: Marketing, promotions, and occupancy acceleration.
• Ongoing Facility Management: Staffing, maintenance, revenue optimization.

4. CONTACT
Purpose: Provide simple, direct ways to connect.
Content Highlights:
• Contact Form (Name, Email, Phone, Message)
• Direct Email: info@keystonevaultdepot.com
• Phone (if applicable)
• Google Map embed (if there’s a head office location)
• CTA: “Let’s Build Your Storage Success Story.”
Design & Technical Notes
• Visual Style: Clean, modern, bold typography, professional color palette (to be based on branding), strong imagery of self storage facilities.
• Performance: Image compression, caching, responsive scaling.
• SEO Targets: “Self storage facility developer,” “self storage construction,” “self storage management company,” “lease-up services for self storage.”

WordPress or Joomla – must be desktop and mobile friendly with fast page load speed. Need the ability to edit ourselves.

Use pantone colours - #033c5a – dark blue
#2baadf – light blue

```html
<!DOCTYPE html>
<html lang="en">
<head>
<meta charset="utf-8">
<title>Keystone Vault Depot Services – Self Storage Experts</title>
<link href="https://fonts.googleapis.com/css2?family=Poppins:wght@400;500;600;700&display=swap" rel="stylesheet">
<style>
:root{
  --navy:#033c5a;
  --sky:#2baadf;
  --ink:#0f2433;
  --text:#4a5863;
  --mist:#f3f6f8;
  --field:#f5f7f9;
  --frame:#e4e7e9;
  --white:#ffffff;
  --ghost:#eceff2;
}
*{margin:0;padding:0;box-sizing:border-box}
html,body{width:1200px;height:3934px;overflow:hidden}
body{background:var(--frame);font-family:"Poppins",sans-serif;color:var(--ink)}
.page{position:absolute;left:73px;top:63px;width:1054px;height:3807px;background:var(--white);overflow:hidden}
.abs{position:absolute}
.photo{position:absolute}
.btn{position:absolute;background:var(--sky);color:var(--white);font-size:9px;font-weight:600;letter-spacing:.4px;text-transform:uppercase;display:flex;align-items:center;justify-content:center}
h1,h2,h3{font-weight:700;text-transform:uppercase;letter-spacing:-.3px}
.section-title{position:absolute;left:132px;font-size:27px;color:var(--ink);line-height:1.1}
.body-copy{font-size:10.5px;line-height:17.5px;color:var(--text)}

/* header */
.header{position:absolute;left:0;top:0;width:1054px;height:53px;background:var(--white)}
.brand{position:absolute;left:132px;top:12px;display:flex;align-items:center;gap:8px}
.brand-mark{width:22px;height:22px;background:var(--navy)}
.brand-name{font-size:13px;font-weight:600;color:var(--navy);line-height:1}
.topbar{position:absolute;top:6px;font-size:8px;color:var(--text);display:flex;align-items:center;gap:5px}
.topbar svg{width:9px;height:9px}
.navbar{position:absolute;left:298px;top:32px;width:756px;height:42px;background:var(--sky)}
.nav-link{position:absolute;top:15px;font-size:9.5px;color:var(--white);font-weight:500}
.nav-cta{position:absolute;left:447px;top:6px;width:176px;height:30px;background:var(--navy);color:var(--white);font-size:9px;font-weight:600;display:flex;align-items:center;justify-content:center}

/* hero */
.hero{position:absolute;left:0;top:53px;width:1054px;height:457px}
.hero-title{position:absolute;left:132px;top:179px;font-size:27px;line-height:36px;color:var(--white)}
.hero-copy{position:absolute;left:132px;top:293px;width:420px;font-size:9.5px;line-height:16px;color:#d8e6ee}

/* word band */
.word-band{position:absolute;left:0;width:1054px;height:66px;display:flex;align-items:center;justify-content:center;gap:14px;font-size:60px;font-weight:700;color:var(--ghost);white-space:nowrap;letter-spacing:1px}
.word-band i{display:block;width:48px;height:48px;background:var(--ghost)}

/* why band */
.why{position:absolute;left:0;top:972px;width:1054px;height:217px;background:var(--mist)}
.v-bar{position:absolute;top:0;height:217px;width:50px;background:var(--navy);color:var(--white)}
.v-bar span{position:absolute;left:50%;top:50%;transform:translate(-50%,-50%) rotate(-90deg);white-space:nowrap;font-size:17px;font-weight:700;letter-spacing:.5px}
.stat-box{position:absolute;left:480px;top:0;width:151px;height:217px;background:var(--sky);color:var(--white);text-align:center}
.stat-num{font-size:27px;font-weight:600;line-height:1}
.stat-label{font-size:11px;line-height:16px;color:#e6f5fc}
.point{position:absolute;display:flex;gap:14px;font-size:11px;font-weight:600;line-height:15px;text-transform:uppercase;color:var(--ink)}
.point b{color:var(--sky);font-size:14px;font-style:italic;font-weight:700;line-height:15px}

/* services */
.card{position:absolute;width:389px;height:193px;background:var(--mist)}
.card.dark{background:var(--navy)}
.card .photo{left:0;top:0;width:133px;height:193px}
.card h3{position:absolute;left:169px;top:36px;font-size:12.5px;line-height:18px;color:var(--navy)}
.card.dark h3{color:var(--white)}
.card p{position:absolute;left:169px;top:82px;width:195px;font-size:9px;line-height:14px;color:var(--text)}
.card.dark p{color:#d4e3ec}
.card .btn{left:169px;top:129px;width:100px;height:24px;font-size:8px}

/* cta */
.cta{position:absolute;left:0;top:1913px;width:1054px;height:302px;background:var(--mist)}
.cta h2{position:absolute;left:132px;top:65px;font-size:22px;line-height:29px;color:var(--ink)}

/* projects */
.proj{position:absolute}
.caption{position:absolute;left:408px;top:2700px;width:238px;height:88px;background:var(--white);text-align:center;padding-top:14px}
.caption h3{font-size:14px;font-weight:600;color:var(--ink)}
.caption p{font-size:9px;line-height:14px;color:var(--text);margin-top:6px}

/* contact */
.field{position:absolute;background:var(--field);font-size:11px;color:var(--text);padding:14px 0 0 18px}

/* footer */
.footer{position:absolute;left:0;top:3513px;width:1054px;height:294px;background:var(--navy);color:var(--white)}
.f-head{position:absolute;top:56px;font-size:12px;font-weight:600}
.f-list{position:absolute;top:87px;font-size:9.5px;line-height:24px;color:#d5e2ea;list-style:none}
.f-contact{position:absolute;left:753px;display:flex;align-items:center;gap:12px;font-size:9.5px;color:#d5e2ea}
.f-icon{width:18px;height:18px;background:var(--sky);display:flex;align-items:center;justify-content:center}
.f-icon svg{width:10px;height:10px}
.social{position:absolute;top:201px;width:28px;height:28px;background:var(--sky)}
</style>
</head>
<body>
<main class="page">

  <!-- hero -->
  <section class="hero">
    <svg class="abs" width="1054" height="457" viewBox="0 0 1054 457">
      <defs>
        <linearGradient id="heroShade" x1="0" y1="0" x2="1" y2="0">
          <stop offset="0" stop-color="#033c5a"/>
          <stop offset="1" stop-color="#0a4e72"/>
        </linearGradient>
      </defs>
      <rect width="1054" height="457" fill="url(#heroShade)"/>
      <circle cx="60" cy="60" r="32" fill="#ffffff" opacity=".06"/>
      <circle cx="38" cy="90" r="22" fill="#ffffff" opacity=".05"/>
    </svg>
    <div class="photo" role="img" aria-label="Bright interior corridor of a modern self storage facility with roll-up doors and cardboard boxes" style="left:0;top:0;width:1054px;height:457px;clip-path:polygon(700px 0,1054px 0,1054px 457px,500px 457px);background:linear-gradient(120deg,#cdd3d8 0%,#eef0f2 40%,#9aa3ab 75%,#c9ced3 100%)"></div>
    <svg class="abs" width="1054" height="457" viewBox="0 0 1054 457">
      <polygon points="690,40 712,40 512,457 490,457" fill="#2baadf"/>
    </svg>
    <h1 class="hero-title">From Concept To<br>Capacity – Your Self<br>Storage Experts</h1>
    <p class="hero-copy">Keystone Vault Depot Services Delivers Turnkey Design, Construction, Leasing, And Management Services For Profitable Self Storage Operations</p>
    <span class="btn" style="left:132px;top:355px;width:105px;height:29px">Learn More</span>
  </section>

  <!-- header -->
  <header class="header">
    <div class="brand"><span class="brand-mark"></span><span class="brand-name">Keystone Vault Depot Services</span></div>
    <div class="topbar" style="left:359px">
      <svg viewBox="0 0 10 10"><path d="M5 0.5a3.3 3.3 0 0 0-3.3 3.3C1.7 6.3 5 9.5 5 9.5s3.3-3.2 3.3-5.7A3.3 3.3 0 0 0 5 .5zm0 4.6a1.3 1.3 0 1 1 0-2.6 1.3 1.3 0 0 1 0 2.6z" fill="#2baadf"/></svg>
      Lorem Ipsum Dolor Sit Amet Consectetur.
    </div>
    <div class="topbar" style="left:556px">
      <svg viewBox="0 0 10 10"><rect x="0.5" y="1.5" width="9" height="7" rx="1" fill="#2baadf"/></svg>
      info@keystonevaultdepot.com
    </div>
    <div class="topbar" style="left:837px">
      <svg viewBox="0 0 10 10"><path d="M2.2.8l1.6 2-1 1.1a6 6 0 0 0 3.3 3.3l1.1-1 2 1.6-.9 1.4C4.6 9 1 5.4.8 2.1z" fill="#2baadf"/></svg>
      +(000)-000-0000
    </div>
    <nav class="navbar">
      <span class="nav-link" style="left:58px">Home</span>
      <span class="nav-link" style="left:122px">About Us</span>
      <span class="nav-link" style="left:200px">Services ⌄</span>
      <span class="nav-link" style="left:286px">Projects</span>
      <span class="nav-link" style="left:359px">Contact</span>
      <span class="nav-cta">REQUEST A CONSULTATION</span>
    </nav>
  </header>

  <div class="word-band" style="top:525px">KEYSTONE VAULT <i></i> DEPOT SERVICES</div>

  <!-- who we are -->
  <h2 class="section-title" style="top:682px">Who We Are</h2>
  <p class="body-copy abs" style="left:132px;top:733px;width:340px">Lorem Ipsum Dolor Sit Amet Consectetur. Semper Nisl Nisi Id Aenean. Etiam Malesuada Gravida Nunc Integer Suscipit Scelerisque Mi Morbi. Id Elementum Porta Sit Nunc Vel Fermentum. Tempus Nam Nunc Tellus Eget Interdum.</p>
  <span class="btn" style="left:132px;top:823px;width:156px;height:27px">Learn More About Us</span>
  <div class="photo" role="img" aria-label="Steel frame of a storage building under construction with two workers in safety vests" style="left:498px;top:650px;width:425px;height:240px;background:linear-gradient(180deg,#4f8fd0 0%,#8fbce6 45%,#8c8577 70%,#c4a77a 100%)"></div>
  <svg class="abs" style="left:860px;top:650px" width="140" height="320" viewBox="0 0 140 320">
    <polygon points="100,0 112,0 66,110 54,110" fill="#2baadf"/>
    <polygon points="86,55 98,55 52,170 40,170" fill="#033c5a"/>
    <polygon points="114,108 126,108 78,220 66,220" fill="#2baadf"/>
    <polygon points="52,220 62,220 34,282 24,282" fill="#033c5a"/>
    <polygon points="62,232 72,232 24,322 14,322" fill="#2baadf"/>
  </svg>

  <!-- why choose us / approach -->
  <section class="why">
    <svg class="abs" style="left:0;top:20px" width="90" height="200" viewBox="0 0 90 200">
      <polygon points="70,0 82,0 10,185 0,185 0,175" fill="#2baadf"/>
      <polygon points="80,55 92,55 28,197 16,197" fill="#033c5a"/>
      <polygon points="88,110 96,110 52,197 40,197" fill="#2baadf"/>
    </svg>
    <div class="v-bar" style="left:132px"><span>WHY CHOOSE US</span></div>
    <div class="point" style="left:209px;top:40px"><b>//</b><span>Industry Expertise In Self<br>Storage</span></div>
    <div class="point" style="left:209px;top:92px"><b>//</b><span>Proven Track Record In<br>Lease-Up Success</span></div>
    <div class="point" style="left:209px;top:144px"><b>//</b><span>Strong Vendor And<br>Contractor Network</span></div>
    <div class="stat-box">
      <div class="stat-num" style="margin-top:30px">50+</div>
      <div class="stat-label" style="margin-top:6px">Completed<br>Storage Facilities</div>
      <div class="stat-num" style="margin-top:18px">95%</div>
      <div class="stat-label" style="margin-top:6px">Average Lease-Up<br>Success Rate</div>
    </div>
    <div class="v-bar" style="left:631px"><span>OUR APPROACH</span></div>
    <div class="point" style="left:709px;top:40px"><b>//</b><span>Lorem Ipsum Dolor Sit Amet<br>Consectetur. Sit.</span></div>
    <div class="point" style="left:709px;top:92px"><b>//</b><span>Proven Track Record In<br>Lease-Up Success</span></div>
    <div class="point" style="left:709px;top:144px"><b>//</b><span>Lorem Ipsum Dolor Sit Amet<br>Consectetur.</span></div>
  </section>

  <!-- services -->
  <h2 class="section-title" style="top:1267px">Our Services</h2>
  <p class="body-copy abs" style="left:661px;top:1270px;width:270px;font-size:9.5px;line-height:17px">Lorem Ipsum Dolor Sit Amet Consectetur Semper Nisl Nisi Id Aenean. Etiam Malesuada.</p>

  <article class="card dark" style="left:132px;top:1343px">
    <div class="photo" role="img" aria-label="Blue metal storage building with roll-up doors under a clear sky" style="background:linear-gradient(180deg,#6aa6dc 0%,#2a5f9e 55%,#9a9a8f 100%)"></div>
    <h3>Facility Design &amp;<br>Development</h3>
    <p>Lorem Ipsum Dolor Sit Amet Semper Nisl Nisi Id Aenean Etiam.</p>
    <span class="btn">Learn More</span>
  </article>
  <article class="card" style="left:535px;top:1343px">
    <div class="photo" role="img" aria-label="Two builders in safety vests in front of a steel building frame" style="background:linear-gradient(180deg,#6aa2d6 0%,#8a8e93 50%,#b99c70 100%)"></div>
    <h3>Construction &amp; Build<br>Management</h3>
    <p>Lorem Ipsum Dolor Sit Amet Semper Nisl Nisi Id Aenean Etiam.</p>
    <span class="btn">Learn More</span>
  </article>
  <article class="card" style="left:132px;top:1551px">
    <div class="photo" role="img" aria-label="Team members around a desk with laptops and marketing plans" style="background:linear-gradient(160deg,#e8e6e1 0%,#c9c2b6 50%,#8d8a85 100%)"></div>
    <h3>Lease-Up &amp;<br>Marketing</h3>
    <p>Lorem Ipsum Dolor Sit Amet Semper Nisl Nisi Id Aenean Etiam.</p>
    <span class="btn">Learn More</span>
  </article>
  <article class="card" style="left:535px;top:1551px">
    <div class="photo" role="img" aria-label="Facility staff reviewing a tablet beside green storage unit doors" style="background:linear-gradient(180deg,#7fa36a 0%,#c9b48f 55%,#6f7a57 100%)"></div>
    <h3>Ongoing Facility<br>Management</h3>
    <p>Lorem Ipsum Dolor Sit Amet Semper Nisl Nisi Id Aenean Etiam.</p>
    <span class="btn">Learn More</span>
  </article>

  <div class="word-band" style="top:1795px">KEYSTONE VAULT <i></i> DEPOT SERVICES</div>

  <!-- contact banner -->
  <section class="cta">
    <div class="photo" role="img" aria-label="Long row of self storage units with blue doors under a blue sky" style="left:0;top:0;width:1054px;height:302px;clip-path:polygon(620px 0,1054px 0,1054px 302px,445px 302px);background:linear-gradient(180deg,#3d78c2 0%,#a6c7ea 45%,#d9dde2 65%,#8d9196 100%)"></div>
    <svg class="abs" width="1054" height="302" viewBox="0 0 1054 302">
      <polygon points="610,12 624,12 458,302 444,302" fill="#2baadf"/>
      <polygon points="74,0 86,0 8,200 0,200 0,180" fill="#2baadf"/>
      <polygon points="86,40 98,40 6,275 0,275 0,262" fill="#033c5a"/>
      <polygon points="95,85 107,85 10,302 0,302" fill="#2baadf"/>
    </svg>
    <h2>Ready To Build Your Next<br>Self Storage Project?<br>Let’s Talk</h2>
    <p class="body-copy abs" style="left:132px;top:166px;width:330px;font-size:9.5px;line-height:16px">Lorem Ipsum Dolor Sit Amet Consectetur Semper Nisl Id Aenean. Etiam Malesuada.</p>
    <span class="btn" style="left:132px;top:207px;width:108px;height:28px">Contact Us</span>
  </section>

  <!-- featured projects -->
  <h2 class="section-title" style="top:2292px">Featured Projects</h2>
  <p class="body-copy abs" style="left:132px;top:2339px;width:460px;font-size:9.5px;line-height:16px">See Some Of Our Recent Self-Storage Facility Projects. Each Project Highlights Our Expertise In Design, Construction, Lease-Up, And Facility Management.</p>
  <span class="btn" style="left:787px;top:2319px;width:139px;height:27px">View All Projects</span>

  <div class="proj photo" role="img" aria-label="Storage building with light blue roll-up doors, one open" style="left:132px;top:2414px;width:256px;height:246px;background:linear-gradient(135deg,#dfe3e6 0%,#9fb3c6 45%,#4f7fb0 100%)"></div>
  <div class="proj photo" role="img" aria-label="Row of storage units with yellow doors" style="left:132px;top:2672px;width:256px;height:128px;background:linear-gradient(180deg,#9ec3e8 0%,#c9ccce 50%,#c9b23a 100%)"></div>
  <div class="proj photo" role="img" aria-label="Storage building with red roll-up doors on an asphalt lot" style="left:399px;top:2414px;width:256px;height:386px;background:linear-gradient(180deg,#8fb6df 0%,#cfd6dc 30%,#c9463f 55%,#5e6165 100%)"></div>
  <div class="caption"><h3>PROJECTS 01</h3><p>Lorem Ipsum Dolor Sit Amet Nisl Id<br>Aenean. Etiam Malesuada.</p></div>
  <div class="proj photo" role="img" aria-label="Modern storage facility exterior with blue doors" style="left:666px;top:2414px;width:257px;height:129px;background:linear-gradient(180deg,#6f9fd4 0%,#d6dade 55%,#3d6fb0 100%)"></div>
  <div class="proj photo" role="img" aria-label="Long driveway between rows of red-door storage units under clouds" style="left:666px;top:2556px;width:257px;height:244px;background:linear-gradient(180deg,#b8c9da 0%,#e2e5e8 40%,#b85a50 65%,#77797c 100%)"></div>

  <!-- contact -->
  <h2 class="abs" style="left:0;width:1054px;top:2893px;text-align:center;font-size:27px;line-height:35px;color:var(--ink)">Let’s Build Your Storage<br>Success Story</h2>
  <p class="body-copy abs" style="left:0;width:1054px;top:2960px;text-align:center;font-size:9.5px;line-height:16px">Have Questions Or Ready To Start Your Next Self-Storage Project? Get In Touch With Our<br>Team Today — We’re Here To Help.</p>

  <div class="abs" style="left:147px;top:3090px;width:6px;height:207px;background:var(--navy)"></div>
  <div class="photo" role="img" aria-label="Street map marking the head office location" style="left:153px;top:3040px;width:321px;height:305px;background:linear-gradient(135deg,#eef0f3 0%,#e3e7ec 50%,#d9dee4 100%)"></div>

  <div class="field" style="left:516px;top:3041px;width:190px;height:38px">Name</div>
  <div class="field" style="left:716px;top:3041px;width:188px;height:38px">Email</div>
  <div class="field" style="left:516px;top:3092px;width:190px;height:38px">Phone</div>
  <div class="field" style="left:716px;top:3092px;width:188px;height:38px">Address</div>
  <div class="field" style="left:516px;top:3140px;width:388px;height:98px">Message</div>
  <div class="abs" style="left:517px;top:3270px;width:15px;height:15px;border:1.5px solid #55626c"></div>
  <p class="body-copy abs" style="left:550px;top:3262px;width:360px;font-size:9.5px;line-height:16px">Lorem Ipsum Dolor Sit Amet Consectetur. Odio Eget Semper Congue Non Sed. Blandit Vitae Amet Turpis.</p>
  <span class="btn" style="left:516px;top:3318px;width:109px;height:27px">Contact Us</span>
  <svg class="abs" style="left:851px;top:2930px" width="110" height="310" viewBox="0 0 110 310">
    <polygon points="10,0 20,0 108,190 98,190" fill="#2baadf"/>
    <polygon points="0,45 12,45 70,165 58,165" fill="#033c5a"/>
    <polygon points="55,130 66,130 110,225 99,225" fill="#033c5a"/>
    <polygon points="42,165 53,165 110,300 99,300" fill="#2baadf"/>
  </svg>

  <div class="word-band" style="top:3400px">KEYSTONE VAULT <i></i> DEPOT SERVICES</div>

  <!-- footer -->
  <footer class="footer">
    <div class="abs" style="left:132px;top:57px;display:flex;align-items:center;gap:8px">
      <span style="width:24px;height:24px;background:var(--white)"></span>
      <span style="font-size:13px;font-weight:600;line-height:1">Keystone Vault Depot Services</span>
    </div>
    <p class="abs" style="left:132px;top:115px;width:230px;font-size:9.5px;line-height:16px;color:#d5e2ea">Lorem Ipsum Dolor Sit Amet Consectetur Vitae Duis Sit Facilisi Fermentum.</p>
    <span class="social" style="left:132px"></span>
    <span class="social" style="left:168px"></span>
    <span class="social" style="left:204px"></span>

    <h4 class="f-head" style="left:425px">LINKS</h4>
    <ul class="f-list" style="left:425px"><li>Home</li><li>About Us</li><li>Services ⌄</li><li>Projects</li><li>Contact</li></ul>

    <h4 class="f-head" style="left:539px">SERVICES</h4>
    <ul class="f-list" style="left:539px"><li>Design &amp; Development</li><li>Construction Management</li><li>Lease-Up Strategy</li><li>Ongoing Facility Management</li></ul>

    <h4 class="f-head" style="left:753px">CONTACT US</h4>
    <div class="f-contact" style="top:94px"><span class="f-icon"><svg viewBox="0 0 10 10"><path d="M2.2.8l1.6 2-1 1.1a6 6 0 0 0 3.3 3.3l1.1-1 2 1.6-.9 1.4C4.6 9 1 5.4.8 2.1z" fill="#fff"/></svg></span>+(000)+000-0000</div>
    <div class="f-contact" style="top:124px"><span class="f-icon"><svg viewBox="0 0 10 10"><path d="M5 .5a3.3 3.3 0 0 0-3.3 3.3C1.7 6.3 5 9.5 5 9.5s3.3-3.2 3.3-5.7A3.3 3.3 0 0 0 5 .5zm0 4.6a1.3 1.3 0 1 1 0-2.6 1.3 1.3 0 0 1 0 2.6z" fill="#fff"/></svg></span>Lorem Ipsum Dolor Sit Amet.</div>
    <div class="f-contact" style="top:154px"><span class="f-icon"><svg viewBox="0 0 10 10"><rect x=".5" y="1.5" width="9" height="7" rx="1" fill="#fff"/></svg></span>info@keystonevaultdepot.com</div>

    <div class="abs" style="left:132px;top:258px;width:790px;height:1px;background:rgba(255,255,255,.18)"></div>
    <p class="abs" style="left:132px;top:271px;font-size:8px;color:#d5e2ea">Copyright © 2025 Keystone Vault Depot Services . All Rights Reserved.</p>
    <p class="abs" style="left:775px;top:271px;width:147px;text-align:right;font-size:8px;color:#d5e2ea">Privacy Policy &amp; Terms Of Condition</p>
  </footer>
</main>
</body>
</html>
```